Completely Coded Dog Community Website - Mobile Centric & Highly Responsive

We need a completely coded design based in Wordpress CMS that is designed with mobile in mind first! I would like to carry over the style of our current website (brightkennels.c0m) into the design of the responsive website. In addition, please only submit designs if you provide high quality admin support, as the winning design will likely be hired to provide monthly support forward at $100/month (SEO skill set valued). Also am looking for a quote on an iphone and android app so please submit designs only if you have capability to create the highest quality apps. No cheap looking template submissions please...will need form, chat, sign in and e-commerce integration. I have vector files if needed for website.
Updates

Project Deadline Extended
Reason: Want to see more mobile friendly, modern designs and responses to willingness for web admin support going forward. Thanks

Target Market(s)

Adults based in the USA aged 25-50 that own dogs

Industry/Entity Type

E-Commerce

Requirements
Must have
• Pages:
Home Page
About Us
Contact Us
Dog Deals
Videos
Photos
Health
Training
Breeds
Ask the Dog Expert
Dog Product Reviews
Dog Stories
Dog Friendly Travel
Dog Care
Contests
Nice to have
• SEO
Metatags
Unique page layouts
Social integration to our social media accounts
Social API logins
Should not have
• Cheap template look
Not consistent with previous color scheme
Different logo than our current options

```html
<!DOCTYPE html>
<html lang="en">
<head>
<meta charset="utf-8">
<title>Bright Kennels – Dog Community</title>
<link href="https://fonts.googleapis.com/css2?family=Open+Sans:wght@400;600;700&family=Open+Sans+Condensed:wght@700&display=swap" rel="stylesheet">
<style>
:root{
  --orange:#f6a431;
  --orange-deep:#ec8f1c;
  --orange-pale:#fbd9a0;
  --teal:#2f8094;
  --teal-dark:#1f6375;
  --teal-light:#3d93a8;
  --charcoal:#3d3d3d;
  --charcoal-dark:#262626;
  --page:#f0f0f0;
  --white:#ffffff;
  --ink:#333333;
  --muted:#6b6b6b;
  --green:#6bb82e;
  --rule:#d8d8d8;
}
*{box-sizing:border-box;margin:0;padding:0}
html,body{width:862px;height:1200px;overflow:hidden}
body{
  position:relative;font-family:"Open Sans",Arial,sans-serif;color:var(--ink);
  background:linear-gradient(to bottom,var(--orange) 0 150px,#4a4a4a 150px,#2e2e2e 900px,var(--orange-pale) 900px 1164px,var(--charcoal-dark) 1164px);
}
.page{position:absolute;left:112px;top:24px;width:641px;height:1140px;background:var(--page);box-shadow:0 0 18px rgba(0,0,0,.45)}
.abs{position:absolute}

/* top bar */
.topbar{left:0;top:0;width:641px;height:24px;background:var(--teal);display:flex;align-items:center}
.search{position:absolute;left:232px;top:4px;width:134px;height:17px;background:var(--white);border:1px solid #9cc;font-size:8px;color:#888;padding:2px 4px}
.search svg{position:absolute;right:3px;top:3px}
.toplinks{position:absolute;left:372px;top:0;height:24px;display:flex;align-items:center;gap:7px;font-size:8px;font-weight:700;color:var(--white);text-transform:uppercase}

/* header */
.brand{left:24px;top:36px;display:flex;align-items:center;gap:6px}
.brand-dot{width:30px;height:30px;border-radius:50%;background:var(--orange)}
.brand-name{font-size:20px;font-weight:700;color:var(--teal)}
.call{left:314px;top:55px;width:126px;height:36px;background:var(--green);border-radius:3px;color:var(--white);text-align:center}
.call small{display:block;font-size:9px;padding-top:3px}
.call strong{display:block;font-size:16px;line-height:18px}
.agent{left:440px;top:44px;width:42px;height:50px;background:linear-gradient(#e8d8c8,#9c8a7a);border-radius:3px}
.account{left:490px;top:44px;font-size:8px;color:var(--ink);display:flex;gap:6px;align-items:center}
.sel{display:inline-block;background:var(--teal);color:#fff;padding:0 4px;font-size:8px;border-radius:2px}
.cart{left:508px;top:74px;font-size:9px;display:flex;gap:4px;align-items:center}

/* nav */
.nav{left:0;top:100px;width:641px;height:29px;background:var(--teal);display:flex}
.nav a{color:var(--white);font-size:8.5px;font-weight:700;text-transform:uppercase;text-decoration:none;padding:0 6px;display:flex;align-items:center;border-right:1px solid var(--teal-light)}
.nav a.current{background:var(--orange)}
.nav a:last-child{border-right:0}

/* hero */
.hero{left:0;top:136px;width:641px;height:236px;background:linear-gradient(to bottom,#fff6ea,#fbd7a6);overflow:hidden}
.hero-photo{position:absolute;left:0;top:50px;width:455px;height:186px;background:linear-gradient(to right,#b87a4c,#8e6040,#c9a47c,#9b7456);opacity:.8}
.offer{position:absolute;left:348px;top:28px;color:var(--ink)}
.offer h2{font-weight:400;font-size:25px;letter-spacing:.5px;line-height:28px}
.offer .save{font-size:50px;line-height:52px;color:var(--teal);font-weight:400}
.offer .save b{color:var(--ink);font-weight:700}
.offer p{font-size:13px}
.btn{display:inline-block;background:var(--teal);color:var(--white);font-weight:700;text-transform:uppercase;text-align:center}
.offer .btn{margin-top:8px;width:88px;height:26px;line-height:26px;font-size:10px;border-radius:2px}
.dots{position:absolute;right:14px;bottom:8px;display:flex;gap:3px}
.dots i{width:7px;height:7px;border-radius:50%;background:#8a5a2a}
.dots i:first-child{background:var(--orange-deep)}

/* welcome & ad */
.welcome{left:0;top:380px;width:402px;height:96px;background:var(--white);border:1px solid var(--rule)}
.welcome-photo{position:absolute;left:4px;top:4px;width:148px;height:86px;background:linear-gradient(#f4f0ea,#c89a6c);border-radius:2px}
.welcome-text{position:absolute;left:154px;top:8px;width:240px}
.welcome-text h3{font-size:14px;font-weight:400}
.welcome-text h3 span{color:var(--teal);font-weight:600}
.welcome-text p{font-size:7.5px;line-height:11px;color:var(--muted);margin-top:3px}
.more{position:absolute;right:8px;bottom:4px;font-size:7.5px;color:var(--teal);font-weight:700}
.ad{left:408px;top:380px;width:188px;height:96px;background:linear-gradient(to right,#2a2a2a,#5a4030);color:var(--white)}
.ad p{position:absolute;left:6px;top:4px;font-size:9px;font-style:italic}
.ad strong{position:absolute;left:8px;top:14px;font-size:22px}
.ad em{position:absolute;left:10px;top:40px;font-size:10px;font-style:normal}
.ad small{position:absolute;left:0;bottom:0;width:100%;text-align:center;font-size:7px;background:#111;padding:2px 0}

/* sidebar */
.panel-head{background:linear-gradient(var(--teal-light),var(--teal-dark));color:var(--white);font-size:10px;font-weight:600;text-transform:uppercase;padding:0 8px;height:20px;line-height:20px}
.popular{left:0;top:485px;width:144px;background:var(--white);box-shadow:0 2px 4px rgba(0,0,0,.25)}
.popular ul{list-style:none}
.popular li{font-size:8px;line-height:10px;padding:5px 8px;height:34px;border-bottom:1px solid var(--rule);display:flex;align-items:center}
.popular li.active{background:var(--orange)}
.popular li:last-child{border:0}
.promo{left:0;top:822px;width:144px;height:136px;background:var(--white);border:1px solid var(--rule)}
.promo h4{background:var(--teal-dark);color:var(--white);font-size:10px;font-weight:700;text-align:center;height:18px;line-height:18px}
.promo h4 b{color:var(--orange)}
.promo-photo{height:94px;background:linear-gradient(#d8c0a8,#c06050)}
.promo .btn{display:block;background:var(--orange);color:var(--ink);font-size:11px;height:22px;line-height:22px}

/* featured */
.featured-head{left:151px;top:485px;width:445px;display:flex;justify-content:space-between}
.cards{left:151px;top:520px;width:445px;display:grid;grid-template-columns:repeat(3,144px);column-gap:6px;row-gap:14px}
.card{background:var(--white);height:176px;padding:4px;box-shadow:0 1px 4px rgba(0,0,0,.2)}
.card-photo{position:relative;height:114px}
.card-photo span{position:absolute;left:0;bottom:0;width:100%;background:rgba(0,0,0,.55);color:var(--white);font-size:8px;font-weight:700;padding:3px 5px}
.card p{font-size:7.5px;line-height:10px;color:var(--muted);margin:3px 2px}
.card .btn{display:block;background:var(--orange);color:var(--ink);font-size:11px;font-weight:400;height:22px;line-height:22px}
.card .btn.alt{background:var(--teal);color:var(--white)}
.p1{background:linear-gradient(#e2c9a0,#b77a3a)}
.p2{background:linear-gradient(#6f9a7a,#3e4a3a)}
.p3{background:linear-gradient(#5a4e44,#c8a070)}
.p4{background:linear-gradient(#e8e0d4,#8a5030)}
.p5{background:linear-gradient(#3f8ab0,#e6dccc)}
.p6{background:linear-gradient(#8fae6a,#e0b870)}
.shop{left:151px;top:898px;width:445px;height:60px;background:linear-gradient(to right,#6a4a20,#8a6a30,#b86a20,#d0a030);color:var(--white)}
.shop h3{position:absolute;left:12px;top:6px;font-size:24px;font-weight:700}
.shop p{position:absolute;left:12px;top:36px;font-size:8.5px}
.shop .btn{position:absolute;right:14px;top:14px;width:108px;height:30px;line-height:30px;background:var(--orange);color:var(--ink);font-size:12px;font-weight:600;border:1px solid #b96e0e}

/* footer */
.footer{left:0;top:976px;width:641px;height:122px;background:var(--white);padding:12px 18px;display:flex;font-size:8px}
.footer h5{font-size:10px;font-weight:400;text-transform:uppercase;margin-bottom:6px}
.footer ul{list-style:none;line-height:12.5px}
.footer li::before{content:"• "}
.qlinks{width:250px;border-right:1px solid var(--rule)}
.qcols{display:flex;gap:10px}
.policies{width:120px;border-right:1px solid var(--rule);padding-left:18px}
.connect{padding-left:20px}
.socials{display:flex;gap:10px;margin-bottom:10px}
.socials i{width:29px;height:29px;border-radius:50%;background:var(--teal)}
.newsletter{display:flex}
.newsletter span{width:152px;height:18px;border:1px solid var(--rule);color:#999;padding:3px 5px;font-size:8px}
.newsletter b{background:var(--teal);color:var(--white);font-size:8.5px;padding:0 6px;line-height:18px}
.accept{left:0;top:1098px;width:641px;height:42px;border-top:1px solid var(--rule);display:flex;align-items:center;padding:0 18px;gap:10px}
.accept h5{font-size:10px;font-weight:400}
.badges{display:flex;gap:12px}
.badges i{width:28px;height:17px;background:#e8e8e8;border:1px solid #cfcfcf;border-radius:2px}
.accept p{font-size:6.8px;line-height:9px;font-style:italic;color:var(--muted);width:280px}
.bottom{position:absolute;left:0;top:1164px;width:862px;height:36px;color:#ddd;font-size:8px;text-align:center;line-height:36px}
.bottom b{color:var(--orange)}
</style>
</head>
<body>
<div class="page">
  <div class="abs topbar">
    <div class="search">Search
      <svg width="9" height="9" viewBox="0 0 10 10"><circle cx="4" cy="4" r="3" fill="none" stroke="#555" stroke-width="1.4"/><line x1="6.2" y1="6.2" x2="9" y2="9" stroke="#555" stroke-width="1.6"/></svg>
    </div>
    <nav class="toplinks"><span>Dog Care</span>•<span>Contests</span>•<span>Dog Friendly Travel</span>•<span>Contact Us</span></nav>
  </div>

  <div class="abs brand"><span class="brand-dot"></span><span class="brand-name">BrightKennels.c0m</span></div>
  <div class="abs call"><small>CALL US NOW</small><strong>012 555 0199</strong></div>
  <div class="abs agent" role="img" aria-label="Support agent with headset"></div>
  <div class="abs account">
    <svg width="8" height="9" viewBox="0 0 8 9"><rect x="1" y="4" width="6" height="5" fill="#2f8094"/><path d="M2 4V2.5a2 2 0 0 1 4 0V4" fill="none" stroke="#2f8094"/></svg>
    LOGIN | SIGN UP <span>$ <i class="sel">▾</i></span><span>En <i class="sel">▾</i></span>
  </div>
  <div class="abs cart">
    <svg width="12" height="10" viewBox="0 0 12 10"><path d="M0 1h2l2 6h6l1.5-4.5H3" fill="none" stroke="#333"/><circle cx="5" cy="9" r="1" fill="#333"/><circle cx="9" cy="9" r="1" fill="#333"/></svg>
    Cart: 0 ITEM(S) $0.00
  </div>

  <nav class="abs nav">
    <a class="current">Home</a><a>About Us</a><a>Dog Deals</a><a>Videos</a><a>Photos</a><a>Health</a><a>Training</a><a>Breeds</a><a>Ask the Dog Expert</a><a>Dog Product Reviews</a><a>Dog Stories</a>
  </nav>

  <section class="abs hero">
    <div class="hero-photo" role="img" aria-label="Row of dogs of different breeds sitting beside a basket of bones"></div>
    <div class="offer">
      <h2>OFFER OF THE WEEK</h2>
      <div class="save">SAVE <b>20%</b></div>
      <p>on food products</p>
      <span class="btn">Shop Now</span>
    </div>
    <div class="dots"><i></i><i></i><i></i></div>
  </section>

  <section class="abs welcome">
    <div class="welcome-photo" role="img" aria-label="Bulldog eating from a food bowl"></div>
    <div class="welcome-text">
      <h3>Welcome to <span>Bright Kennels</span></h3>
      <p>Lorem ipsum dolor sit amet, consectetuer adipiscing elit, sedfgid diam nonummy nibh euismod tincidunt ut laoreet dolore magna aliquam erat volutpat. Ut wisi enim ad minim veniam, qufihfjhfis nosdghdfghdfdgh trud exerci tation ullamcorper.</p>
    </div>
    <span class="more">more [+]</span>
  </section>
  <aside class="abs ad" role="img" aria-label="Anti-fur campaign banner with a man">
    <p>"If you wouldn't</p><strong>wear</strong><em>your dog...</em><small>PLS... DON'T WEAR ANY FUR</small>
  </aside>

  <aside class="abs popular">
    <div class="panel-head">Most Pawpular</div>
    <ul>
      <li class="active">Demoralized by the charms consequat</li>
      <li>Praising pain was born aspernatur</li>
      <li>Exercitation ullamco laboris</li>
      <li>Demoralized by the charms laboris</li>
      <li>Praising pain was born vel eum</li>
      <li>Exercitation ullamco laboris vel eum</li>
      <li>Praising pain was born aspernatur</li>
      <li>Demoralized by the charms laboris</li>
      <li>Praising pain was born veldhs eum</li>
    </ul>
  </aside>
  <aside class="abs promo">
    <h4>GET <b>30%</b> DISCOUNT ON FOOD</h4>
    <div class="promo-photo" role="img" aria-label="Dachshund beside a bowl of dog food"></div>
    <span class="btn">Shop Now</span>
  </aside>

  <div class="abs panel-head featured-head"><span>Featured Puppies</span>
    <svg width="20" height="12" viewBox="0 0 20 12"><path d="M7 2 3 6l4 4M13 2l4 4-4 4" fill="none" stroke="#fff" stroke-width="1.6"/></svg>
  </div>
  <section class="abs cards">
    <article class="card"><div class="card-photo p1" role="img" aria-label="Tan puppy"><span>Lorem ipsum dolor</span></div><p>Lorem ipsum dolor sit amet, consectetuer adipiscing elit, sed.</p><span class="btn">Vote Now</span></article>
    <article class="card"><div class="card-photo p2" role="img" aria-label="Husky on grass"><span>Lorem ipsum dolor</span></div><p>Lorem ipsum dolor sit amet, consectetuer adipiscing elit, sed.</p><span class="btn alt">Vote Now</span></article>
    <article class="card"><div class="card-photo p3" role="img" aria-label="Pug puppy"><span>Lorem ipsum dolor</span></div><p>Lorem ipsum dolor sit amet, consectetuer adipiscing elit, sed.</p><span class="btn">Vote Now</span></article>
    <article class="card"><div class="card-photo p4" role="img" aria-label="Boxer puppy"><span>Lorem ipsum dolor</span></div><p>Lorem ipsum dolor sit amsdfgdsfet, consectetuer adipiscing elit, sed.</p><span class="btn">Vote Now</span></article>
    <article class="card"><div class="card-photo p5" role="img" aria-label="White puppy"><span>Lorem ipsum dolor</span></div><p>Lorem ipsum dolor sit amsdfgsget, consectetuer adipiscing elit, sed.</p><span class="btn">Vote Now</span></article>
    <article class="card"><div class="card-photo p6" role="img" aria-label="Labrador puppy"><span>Lorem ipsum dolor</span></div><p>Lorem ipsum dolor sit amfdgshgdet, consectetuer adipiscing elit, sed.</p><span class="btn">Vote Now</span></article>
  </section>
  <section class="abs shop">
    <h3>SHOP AND SAVE 10%</h3>
    <p>Lorem ipsum dolor sit amet, consectetuer adipiscing elit, sed nonummy.</p>
    <span class="btn">🛒 Shop Now</span>
  </section>

  <footer class="abs footer">
    <div class="qlinks">
      <h5>Quick Links</h5>
      <div class="qcols">
        <ul><li>Home Page</li><li>About Us</li><li>Contact Us</li><li>Dog Deals</li><li>Videos</li><li>Photos</li></ul>
        <ul><li>Health</li><li>Training</li><li>Breeds</li><li>Ask the Dog Expert</li><li>Dog Product Reviews</li><li>Dog Stories</li></ul>
        <ul><li>Dog Friendly Travel</li><li>Dog Care</li><li>Contests</li></ul>
      </div>
    </div>
    <div class="policies">
      <h5>Our Policies</h5>
      <ul><li>Payment Methods</li><li>Shipping &amp; Delivery</li><li>Returns &amp; Exchanges</li><li>Secure Shopping</li><li>Terms &amp; Conditions</li><li>Privacy Policy</li></ul>
    </div>
    <div class="connect">
      <h5>Stay Connected</h5>
      <div class="socials"><i></i><i></i><i></i><i></i></div>
      <h5>Subscribe Newsletter</h5>
      <div class="newsletter"><span>E-mail address</span><b>SUBSCRIBE</b></div>
    </div>
  </footer>
  <div class="abs accept">
    <h5>WE ACCEPT:</h5>
    <div class="badges"><i></i><i></i><i></i><i></i><i></i><i></i></div>
    <p>Lorem ipsum dolor sit amet, consectetur adipiscing elit, sed do eiu dsfysmod tempor incididunt ut labore sit amet, consectetur adipiscing elit, sed do sit amet, cons..</p>
  </div>
</div>
<div class="bottom">© 2015. <b>Bright Kennels</b>. All Rights Reserved.</div>
</body>
</html>
```